Infographic for Ed Non-Profit Showing Parts of a School Design

We need an infographic done that depicts the parts of a school design (or what we call a blueprint). It will be used to help schools understand the different things they need to design and develop to have a coherent school design. These parts include:

Local Context - The larger context in which the learning environment exists.

Purpose - The overarching role the learning environment must play.

Graduate Aims -The learning outcomes the environment will drive toward.

Design Principles - Core characteristics of the learning environment and the experiences learners have within it that weave across the design and help it feel coherent.

Student Experiences - Programmed activities that key stakeholders—such as learners, educators, and families—engage in within the learning environment.

System Elements - The various approaches, structures, and resources related to areas like curriculum, hiring, technology, and more that enable experiences..

Attachments
Internally Created Blueprint Visuals - We have various working drafts that we've done internally but we want to elevate the design now. I've attached these in one document. They show connections between the parts well but are not attractive. The final visual does not need to look like any of these, I am including it just to give an idea of what we've tried. I have a feeling there are lots of other solutions we have not explored yet.

Style Guide - I attached a few pages from our style guide. We do not really have an illustrations or graphic style.

Guide to School Design Blueprint - This is an early draft of one place the infographic will be used. We'd want to put it in the introduction and pieces of it in each of the corresponding sections.

Target Market(s)

School and school system (fdistrict) leaders

Font styles to use
Serif
Other font styles liked:
• Open sans, Bebas Nue, Roberts (see style guide)

Requirements
Must have
• The most critical things are:
1- Include all the parts of a school design (see above).

2- Show how they relate to each other (e.g. system elements enable experiences, experiences drive toward aims, grad aims drive toward purpose, design principles cut across all parts of school design and bring coherence, local context surround the whole school design)
Nice to have
• Pieces of the larger design could be broken or pulled apart and used flexibly. For example, if we want to use the graphic in a deck of slides for an event or in a document we could show the whole graphic or just parts of it.
Should not have
• imagery that is overly stereotypical regarding schools. No old fashioned school houses, no students sitting in row, etc.

```html
<!DOCTYPE html>
<html lang="en">
<head>
<meta charset="utf-8">
<title>Brightfield – Parts of a School Design</title>
<link rel="stylesheet" href="https://fonts.googleapis.com/css2?family=Bebas+Neue&family=Roboto+Condensed:wght@400;700&display=swap">
<style>
  :root {
    --navy: #164a7e;
    --red: #c0000b;
    --red-soft: #ef5a63;
    --sky-top: #b3dcf9;
    --sky-bottom: #f7fbff;
    --ink: #1d1d1d;
    --white: #ffffff;
    --gold: #f7a21b;
  }
  html, body {
    margin: 0;
    padding: 0;
    width: 885px;
    height: 1200px;
    overflow: hidden;
    background: var(--white);
  }
  .infographic { display: block; width: 885px; height: 1200px; }
  .brand-name { font-family: "Roboto Condensed", sans-serif; font-weight: 700; font-size: 52px; fill: var(--red); }
  .pin { fill: var(--navy); }
  .pin-base { fill: var(--gold); }
  .part-heading { font-family: "Bebas Neue", sans-serif; font-size: 23px; fill: var(--white); text-decoration: underline; }
  .part-body { font-family: "Roboto Condensed", sans-serif; font-size: 15px; fill: var(--white); }
  .navy-fill { fill: var(--navy); }
  .target-outer { fill: var(--red); }
  .target-inner { fill: var(--red-soft); }
  .connector { stroke: var(--navy); stroke-width: 1.4; fill: none; }
  .arrow-head { fill: var(--navy); }
  .band { fill: var(--red); }
  .band-title { font-family: "Bebas Neue", sans-serif; font-size: 23px; fill: var(--white); text-decoration: underline; }
  .band-body { font-family: "Roboto Condensed", sans-serif; font-size: 15px; fill: var(--white); }
  .element-line { stroke: var(--red); stroke-width: 1.3; }
  .element-dot { fill: var(--red-soft); stroke: var(--red); stroke-width: 1.5; }
  .gear-teeth { fill: none; stroke: var(--navy); stroke-width: 9; }
  .gear-body { fill: var(--navy); }
  .gear-hub { fill: var(--white); }
  .element-label { font-family: "Roboto Condensed", sans-serif; font-weight: 700; font-size: 13px; fill: var(--ink); }
  .footer-blue { fill: var(--navy); }
  .footer-red { fill: var(--red); }
</style>
</head>
<body>
<svg class="infographic" viewBox="0 0 885 1200" xmlns="http://www.w3.org/2000/svg">
  <defs>
    <linearGradient id="sky" x1="0" y1="0" x2="0" y2="1">
      <stop offset="0" stop-color="var(--sky-top)"/>
      <stop offset="1" stop-color="var(--sky-bottom)"/>
    </linearGradient>
    <linearGradient id="town" x1="0" y1="0" x2="0" y2="1">
      <stop offset="0" stop-color="#ffffff"/>
      <stop offset="0.45" stop-color="#f4f1ea"/>
      <stop offset="1" stop-color="#cfd0d6"/>
    </linearGradient>
    <g id="gear">
      <circle class="gear-teeth" r="31" stroke-dasharray="9.5 9.97"/>
      <circle class="gear-body" r="28"/>
      <circle class="gear-hub" r="17"/>
    </g>
  </defs>

  <!-- Header -->
  <g class="brand">
    <text class="brand-name" x="442" y="80" text-anchor="middle">Brightfield</text>
  </g>

  <!-- Town scene -->
  <rect x="0" y="182" width="885" height="185" fill="url(#town)" role="img" aria-label="Flat illustration of a town skyline with houses, apartment blocks, autumn trees and suns, joined by an arc to a location pin"/>
  <g class="location-pin">
    <path class="pin" d="M442 174 C431 155 421 145 421 127 A21 21 0 0 1 463 127 C463 145 453 155 442 174 Z"/>
    <circle cx="442" cy="127" r="9" fill="#fff"/>
    <ellipse class="pin-base" cx="442" cy="188" rx="18" ry="3.5"/>
  </g>

  <!-- Sky area -->
  <rect x="0" y="367" width="885" height="800" fill="url(#sky)"/>
  <line x1="0" y1="367" x2="885" y2="367" stroke="#3a3f5c" stroke-width="1.2"/>

  <!-- Purpose -->
  <g class="part part-purpose">
    <circle class="target-outer" cx="220" cy="405" r="25"/>
    <circle class="target-inner" cx="220" cy="405" r="17"/>
    <polygon class="navy-fill" points="220,412 128,503 313,503"/>
    <rect class="navy-fill" x="158" y="506" width="124" height="209"/>
    <text class="part-heading" x="220" y="492" text-anchor="middle">PURPOSE</text>
    <text class="part-body" text-anchor="middle">
      <tspan x="220" y="591">The</tspan>
      <tspan x="220" y="609">overarching</tspan>
      <tspan x="220" y="627">role the</tspan>
      <tspan x="220" y="645">learning</tspan>
      <tspan x="220" y="663">environment</tspan>
      <tspan x="220" y="681">must play.</tspan>
    </text>
  </g>

  <!-- Graduate aims -->
  <g class="part part-graduate-aims">
    <circle class="target-outer" cx="442" cy="405" r="25"/>
    <circle class="target-inner" cx="442" cy="405" r="17"/>
    <polygon class="navy-fill" points="442,412 350,503 535,503"/>
    <rect class="navy-fill" x="380" y="506" width="124" height="209"/>
    <text class="part-heading" x="442" y="468" text-anchor="middle">GRADUATE</text>
    <text class="part-heading" x="442" y="492" text-anchor="middle">AIMS</text>
    <text class="part-body" text-anchor="middle">
      <tspan x="442" y="591">The learning</tspan>
      <tspan x="442" y="609">outcomes the</tspan>
      <tspan x="442" y="627">environment</tspan>
      <tspan x="442" y="645">will drive</tspan>
      <tspan x="442" y="663">toward.</tspan>
    </text>
  </g>

  <!-- Student experiences -->
  <g class="part part-student-experiences">
    <circle class="target-outer" cx="663" cy="405" r="25"/>
    <circle class="target-inner" cx="663" cy="405" r="17"/>
    <polygon class="navy-fill" points="663,412 571,503 756,503"/>
    <text class="part-heading" x="663" y="468" text-anchor="middle">STUDENT</text>
    <text class="part-heading" x="663" y="492" text-anchor="middle">EXPERIENCES</text>
    <rect class="navy-fill" x="601" y="506" width="124" height="65"/>
    <rect class="navy-fill" x="601" y="579" width="124" height="64"/>
    <rect class="navy-fill" x="601" y="651" width="124" height="64"/>
    <text class="part-body" text-anchor="middle">
      <tspan x="663" y="526">Programmed</tspan>
      <tspan x="663" y="544">activities that</tspan>
      <tspan x="663" y="562">key stakeholders</tspan>
    </text>
    <text class="part-body" text-anchor="middle">
      <tspan x="663" y="599">Such as learners,</tspan>
      <tspan x="663" y="617">educators, and</tspan>
      <tspan x="663" y="635">families</tspan>
    </text>
    <text class="part-body" text-anchor="middle">
      <tspan x="663" y="671">Engage in within</tspan>
      <tspan x="663" y="689">the learning</tspan>
      <tspan x="663" y="707">environment</tspan>
    </text>
  </g>

  <!-- Relationship arrows -->
  <g class="relationships">
    <line class="connector" x1="380" y1="610" x2="300" y2="610"/>
    <polygon class="arrow-head" points="293,610 307,604 303,610 307,616"/>
    <line class="connector" x1="601" y1="558" x2="518" y2="610"/>
    <line class="connector" x1="601" y1="610" x2="518" y2="610"/>
    <line class="connector" x1="601" y1="663" x2="518" y2="610"/>
    <polygon class="arrow-head" points="511,610 525,604 521,610 525,616"/>
  </g>

  <!-- Foundation bands -->
  <g class="band-local-context">
    <rect class="band" x="129" y="725" width="625" height="33"/>
    <text class="band-title" x="202" y="750">LOCAL CONTEXT</text>
    <text class="band-body" x="322" y="747">-  The larger context in which the learning environment exists.</text>
  </g>
  <g class="band-design-principles">
    <rect class="band" x="79" y="765" width="725" height="46"/>
    <text class="band-title" x="138" y="792">DESIGN PRINCIPLES</text>
    <text class="band-body">
      <tspan x="280" y="786">-  Core characteristics of the learning environment and the experiences learners</tspan>
      <tspan x="292" y="803">have within it that weave across the design and help it feel coherent.</tspan>
    </text>
  </g>
  <g class="band-system-elements">
    <rect class="band" x="29" y="817" width="825" height="47"/>
    <text class="band-title" x="48" y="846">SYSTEM ELEMENTS</text>
    <text class="band-body">
      <tspan x="188" y="839">-  The various approaches, structures, and resources related to areas like curriculum, hiring, technology, and</tspan>
      <tspan x="200" y="856">more that enable experiences..</tspan>
    </text>
  </g>

  <!-- System elements, top row -->
  <g class="system-elements-top">
    <line class="element-line" x1="100" y1="864" x2="100" y2="881"/><circle class="element-dot" cx="100" cy="887" r="6"/>
    <line class="element-line" x1="253" y1="864" x2="253" y2="881"/><circle class="element-dot" cx="253" cy="887" r="6"/>
    <line class="element-line" x1="407" y1="864" x2="407" y2="881"/><circle class="element-dot" cx="407" cy="887" r="6"/>
    <line class="element-line" x1="559" y1="864" x2="559" y2="881"/><circle class="element-dot" cx="559" cy="887" r="6"/>
    <line class="element-line" x1="713" y1="864" x2="713" y2="881"/><circle class="element-dot" cx="713" cy="887" r="6"/>
    <use href="#gear" x="100" y="940"/>
    <use href="#gear" x="253" y="940"/>
    <use href="#gear" x="407" y="940"/>
    <g transform="translate(559 940)">
      <use href="#gear"/>
      <circle r="10" fill="none" stroke="var(--navy)" stroke-width="2.5"/>
      <path d="M0 -6 V0 H5" fill="none" stroke="var(--navy)" stroke-width="2.5"/>
    </g>
    <use href="#gear" x="713" y="940"/>
    <text class="element-label" text-anchor="middle"><tspan x="100" y="994">Community &amp; Family</tspan><tspan x="100" y="1009">Partnerships</tspan></text>
    <text class="element-label" text-anchor="middle"><tspan x="253" y="994">Continuous Learning</tspan><tspan x="253" y="1009">&amp; Improvement</tspan></text>
    <text class="element-label" text-anchor="middle"><tspan x="407" y="994">Technology &amp; Tech</tspan><tspan x="407" y="1009">Infrastructure</tspan></text>
    <text class="element-label" text-anchor="middle"><tspan x="559" y="994">Scheduling &amp;</tspan><tspan x="559" y="1009">Use of Time</tspan></text>
    <text class="element-label" text-anchor="middle"><tspan x="713" y="994">Curriculum, Instruction</tspan><tspan x="713" y="1009">&amp; Assessment</tspan></text>
  </g>

  <!-- System elements, bottom row -->
  <g class="system-elements-bottom">
    <line class="element-line" x1="176" y1="864" x2="176" y2="1025"/><circle class="element-dot" cx="176" cy="1031" r="6"/>
    <line class="element-line" x1="330" y1="864" x2="330" y2="1025"/><circle class="element-dot" cx="330" cy="1031" r="6"/>
    <line class="element-line" x1="483" y1="864" x2="483" y2="1025"/><circle class="element-dot" cx="483" cy="1031" r="6"/>
    <line class="element-line" x1="637" y1="864" x2="637" y2="1025"/><circle class="element-dot" cx="637" cy="1031" r="6"/>
    <line class="element-line" x1="790" y1="864" x2="790" y2="1025"/><circle class="element-dot" cx="790" cy="1031" r="6"/>
    <use href="#gear" x="176" y="1084"/>
    <use href="#gear" x="330" y="1084"/>
    <use href="#gear" x="483" y="1084"/>
    <use href="#gear" x="637" y="1084"/>
    <use href="#gear" x="790" y="1084"/>
    <text class="element-label" text-anchor="middle"><tspan x="176" y="1138">Adult Roles, Hiring</tspan><tspan x="176" y="1153">&amp; Development</tspan></text>
    <text class="element-label" text-anchor="middle"><tspan x="330" y="1138">Space &amp;</tspan><tspan x="330" y="1153">Facilities</tspan></text>
    <text class="element-label" text-anchor="middle"><tspan x="483" y="1138">Budget &amp;</tspan><tspan x="483" y="1153">Operations</tspan></text>
    <text class="element-label" text-anchor="middle"><tspan x="637" y="1138">Communications</tspan></text>
    <text class="element-label" text-anchor="middle"><tspan x="790" y="1138">School Community</tspan><tspan x="790" y="1153">&amp; Culture</tspan></text>
  </g>

  <!-- Footer band -->
  <polygon class="footer-red" points="590,1200 885,1161 885,1200"/>
  <polygon class="footer-blue" points="0,1162 620,1196 590,1200 0,1200"/>
</svg>
</body>
</html>
```